Q.R. Bright Desk Store

The design is for eCommerce home page but I would like it to complement this site: http://www.qrbrightdesksystems.com/ but... it should also have independence as a standalone site.

The best design will be able to effectively mix corporate with a high quality small business consumer feel. It should be completely custom design, not a template look or feel. I want the users to get the feeling that this is the place to go for buying tech for business. We sell the same products as Vantrel.

You can be creative as you wish, as long as the elements of a great eCommerce site are present.

I would like your 'design' to blow these away:
http://www.buying.zorvex.com/
mivoland.com
http://www.vantrel.com/

Here are references:
Call to action
http://trabelwise.com/us/blog/48173-seven-tips-for-designing-an-effective-ecommerce-call-to-action

Effective Ecommerce design
http://www.plov.com/ss/7-tips-for-effective-e-commerce#0

91 points of ecommerce
http://dreb.com/blog/holygrail-of-ecommerce-conversion-optimization-91-points-checklist

UPDATE 07/11/2013:

Please look at the category sample png files. I see already many people are using the main menu from qrbrightdesksystems.com and I do not mind your creativiety, but this is an eCommerce store and people need a menu to get to the categories and/or product types. I don't want to limit anyone creativity by the png samples. I'm also not using them to show I like them in any particular way or form, just that it's needed, whether it's a button (dropdown of course) that says 'Categories' or 'Products, whether it an accordion, horizontal or vertical.

Thanks

UPDATE 07/12/2013:

Please find other use of space that has been used for About Us paragraph (if you've added it to the page). About Us should have it's own page and the purpose of the design should be to sell products (and some services as products). Please put a link or some other creative method to lead users to the About Us page.

Reason: I've raised the award, including 1st, 2nd, and 3rd place and participation payments so I will also extend 7 days. Thanks!

I've updated the product brief. Please scroll down to where it says: UPDATE 07/11/2013

Thanks!

UPDATE 07/12/2013:

Please find other use of space that has been used for About Us paragraph (if you've added it to the page).  About Us should have it's own page and the purpose of the design should be to sell products (and some services as products). Please put a link or some other creative method to lead users to the About Us page if you must but not on the real estate of the page.

Thanks!

Added updates to the brief 7/14/2013.

Thanks!

The voting is in and the project is complete.  Thanks everyone for joining, all of those who participated are truly amazingly talented. But, there were only 3 prizes.  I will be having further projects down the line to develop other pages to this site after the initial implementation is completed.  I truly would like to have you all back. 

- Thank you.

Target Market(s)

corporate decision-makers AND small business consumers

Industry/Entity Type

Small Business

Requirements
Must have
• Call to action.
Openness (non-clutter).

These elements:
Search box
Logo
Tagline
Telephone number
Contact details
Address
My account / sign in
Shopping basket / checkout link
Latest offers
Promotional area
Email sign up
Delivery information
About us
Link to press office / corporate site
Terms and conditions
Sitemap for the footer.
Delivery offers: free
Personalized recommendations
Social media links
Accepted payment methods
Link to blog or community section
Change language / country

http://freshnotesblog.kelvarant.com/sales-leads-landing-page/

UPDATE 07/14/2013
Category Menu. This can be a dropdown, horizontal, vertical, etc. But shoppers need to know how to get to the products they want to buy.
Nice to have
• Trustmarks
Blog/Blog link

UPDATE 07/12/2013:
Make the footer useful.

UPDATE 07/14/2013 (Suggestions of elements to differentiate your designs)

-Quick Shop: A quick buy module/section: Where a user can put in a SKU number or Model number to quickly add the product to their shopping cart.

-Featured
-Best Sellers
-Specials
-Trending Tags/Tag Cloud
- Activity Stream
- Cross Sell/ Up Sell
- Testimonial
- Social Network Feed
- Live Help
- Feedback/Support/Contact Tab
- Show logged in user (i.e. Welcome, Mark Pell)
Should not have
• The design SHOULD NOT be generic like this:

http://www.artflock.com/design/52392
http://www.pelicanvault.com/

The page should not feel over cluttered. It should not have low quality icons or design elements. Navigation should not be hard to discover or confusing.

```html
<!DOCTYPE html>
<html lang="en">
<head>
<meta charset="utf-8">
<title>Q.R. Bright Desk Store</title>
<link href="https://fonts.googleapis.com/css2?family=Barlow:wght@400;500&family=Lato:wght@400;700&family=Arimo:wght@400;700&display=swap" rel="stylesheet">
<style>
:root{
  --blue:#2f9bf0;
  --blue-bright:#1aa6ee;
  --white:#ffffff;
  --page:#ffffff;
  --brand-grey:#c6c6c6;
  --text-grey:#6a6a6a;
  --footer:#393939;
  --footer-deep:#1d1d1d;
  --rule:#262626;
  --rule-light:#4d4d4d;
  --footer-text:#e9e9e9;
  --footer-muted:#b4b4b4;
  --sale:#e02020;
  --panel-border:#dedede;
}
*{box-sizing:border-box;margin:0;padding:0}
html,body{width:1200px;height:900px;overflow:hidden;background:var(--page)}
body{position:relative;font-family:"Arimo",Arial,sans-serif}
.abs{position:absolute}

/* promo strip */
.promo-card{left:61px;top:-2px;width:334px;height:94px;border:1px solid var(--panel-border);border-top:none;background:var(--white)}
.promo-card .product-shot{left:92px;top:0;width:148px;height:18px;background:#111}
.promo-card .caption{left:12px;top:24px;width:200px;font-size:16px;line-height:23px;color:var(--text-grey)}
.promo-card .cta{left:216px;top:18px;width:117px;height:60px;background:var(--blue);color:var(--white);font-weight:700;font-size:16px;line-height:23px;padding:6px 14px}
.deals-panel{left:428px;top:-10px;width:790px;height:96px;border:1px solid var(--panel-border);border-radius:0 0 0 12px;background:var(--white)}
.deal .thumb{width:86px;height:58px}
.deal .title{font-size:14px;line-height:17px;color:#444;width:170px;font-family:"Lato",sans-serif}
.deal .price{font-size:16px;font-weight:700;color:var(--blue)}
.sale-badge{left:490px;top:-18px;width:50px;height:50px;border-radius:50%;background:var(--sale);color:var(--white);font-weight:700;font-size:12px;line-height:13px;text-align:center;padding-top:18px}

/* brand rail */
.brand-rail{left:0;top:140px;width:1200px;height:46px}
.brand-rail .arrow{left:60px;top:2px;font-size:34px;color:var(--brand-grey);font-family:"Barlow",sans-serif}
.brand{top:4px;font-family:"Barlow",sans-serif;font-weight:500;font-size:32px;color:var(--brand-grey);letter-spacing:1px}
.rail-rule{left:62px;top:227px;width:1138px;height:3px;background:var(--blue)}

/* footer */
.site-footer{left:0;top:265px;width:1200px;height:580px;background:var(--footer);border-top:2px solid #c9c9c9;
  background-image:repeating-linear-gradient(45deg,rgba(255,255,255,.018) 0 2px,transparent 2px 4px)}
.footer-base{left:0;top:845px;width:1200px;height:55px;background:var(--footer-deep);border-top:2px solid #4a4a4a}
.col-heading{font-family:"Barlow",sans-serif;font-size:20px;color:var(--footer-text);letter-spacing:.3px;padding-bottom:14px;border-bottom:1px solid var(--rule);box-shadow:0 1px 0 var(--rule-light)}
.col-heading em{font-style:normal;color:var(--blue-bright)}
.heading-icon{display:inline-block;vertical-align:middle;margin-left:14px}
.link-list{list-style:none}
.link-list li{height:39.4px;border-bottom:1px dashed #5a5a5a;font-family:"Lato",sans-serif;font-weight:700;font-size:16px;color:#e0e0e0;padding:14px 14px 0 14px;display:flex;justify-content:space-between}
.link-list li span{color:#9a9a9a;font-weight:400}
.tweet{height:140px;position:relative}
.avatar{position:absolute;left:3px;top:0;width:49px;height:49px;border:2px solid #eee;background:linear-gradient(#d9c5b0,#3b3b44)}
.tweet .name{position:absolute;left:73px;top:6px;font-weight:700;font-size:14px;color:var(--white)}
.tweet .handle{position:absolute;left:73px;top:28px;font-size:14px;color:var(--blue-bright)}
.tweet .date{position:absolute;left:272px;top:28px;font-size:13px;color:#9a9a9a;word-spacing:10px}
.tweet .body{position:absolute;left:2px;top:62px;width:320px;font-size:14px;line-height:16px;color:var(--footer-muted)}
.activity{height:76px;border-bottom:1px dashed #575757;position:relative}
.activity svg{position:absolute;left:6px;top:16px}
.activity .line{position:absolute;left:63px;top:18px;font-size:14px;color:#e0e0e0}
.activity .meta{position:absolute;left:62px;top:41px;font-size:14px;color:#8f8f8f}
.activity .meta b{color:var(--white);margin:0 12px 0 8px}
.activity .meta i{font-style:normal;color:var(--blue-bright)}
.newsletter-text{font-size:14px;line-height:17px;color:var(--footer-muted);white-space:nowrap}
.newsletter-input{width:160px;height:35px;border-radius:5px;background:#2d2d2d;border:1px solid #262626;box-shadow:inset 0 1px 2px rgba(0,0,0,.4)}
.follow{border-top:1px solid #4f4f4f;border-bottom:1px solid #4f4f4f;height:56px;font-family:"Barlow",sans-serif;font-size:14px;color:var(--white);padding-top:19px}
.certificate{left:1037px;top:887px;font-family:"Barlow",sans-serif;font-size:13px;color:#bbb}
.cert-badge{left:1141px;top:866px;width:50px;height:50px;border-radius:50%;background:#e6c432}
</style>
</head>
<body>

<section class="abs promo-card">
  <div class="abs product-shot" role="img" aria-label="Featured desktop tower product photo"></div>
  <p class="abs caption">Lorem ipsum dolor sit amet consectetuer</p>
  <div class="abs cta">$199.99<br>Shop Now</div>
</section>

<section class="abs deals-panel"></section>
<div class="abs deal" style="left:455px;top:0">
  <div class="thumb" role="img" aria-label="CPU cooler product photo" style="background:linear-gradient(#9a9a9a,#333)"></div>
</div>
<div class="abs sale-badge">10%<br>OFF</div>
<div class="abs deal" style="left:551px;top:-8px"><p class="title">Neque porro quisquam est qui rem quisquam</p></div>
<div class="abs deal" style="left:549px;top:35px"><p class="price">$199.99</p></div>

<div class="abs deal" style="left:745px;top:0"><div class="thumb" role="img" aria-label="Monitor product photo" style="background:linear-gradient(#555,#111)"></div></div>
<div class="abs deal" style="left:856px;top:-8px"><p class="title">Neque porro quisquam est qui rem quisquam</p></div>
<div class="abs deal" style="left:856px;top:35px"><p class="price">$199.99</p></div>

<div class="abs deal" style="left:1045px;top:0"><div class="thumb" role="img" aria-label="Gaming tower product photo" style="background:linear-gradient(#3a4a66,#0c0c0c)"></div></div>
<div class="abs deal" style="left:1145px;top:-8px"><p class="title">Neque porro quisquam est qui rem quisquam</p></div>
<div class="abs deal" style="left:1143px;top:35px"><p class="price">$199.99</p></div>

<nav class="abs brand-rail" aria-label="Brands">
  <span class="abs arrow">&lt;</span>
  <span class="abs brand" style="left:133px">Velnor</span>
  <span class="abs brand" style="left:302px">Darkov</span>
  <span class="abs brand" style="left:472px">Astrin</span>
  <span class="abs brand" style="left:640px">Samvero</span>
  <span class="abs brand" style="left:802px">Lentaro</span>
  <span class="abs brand" style="left:999px">Hexpo</span>
  <span class="abs brand" style="left:1150px">Acrel</span>
</nav>
<div class="abs rail-rule"></div>

<footer class="abs site-footer"></footer>

<section class="abs" style="left:60px;top:318px;width:211px">
  <h3 class="col-heading" style="padding-left:15px">LINKS</h3>
  <ul class="link-list" style="margin-left:4px">
    <li>Corporate<span>&gt;</span></li>
    <li>Press Center<span>&gt;</span></li>
    <li>Terms and Coniditions<span>&gt;</span></li>
    <li>Site Map<span>&gt;</span></li>
    <li>Career<span>&gt;</span></li>
    <li>About Us<span>&gt;</span></li>
    <li>Catalog<span>&gt;</span></li>
  </ul>
</section>

<section class="abs" style="left:318px;top:318px;width:331px">
  <h3 class="col-heading" style="padding-left:3px">LATEST <em>TWEETS</em>
    <svg class="heading-icon" width="20" height="18" viewBox="0 0 20 18"><g fill="#777"><rect x="0" y="1" width="18" height="2"/><rect x="0" y="5" width="14" height="2"/><rect x="0" y="9" width="18" height="2"/><rect x="0" y="15" width="2" height="2"/><rect x="4" y="15" width="2" height="2"/><rect x="8" y="15" width="2" height="2"/></g></svg></h3>
  <div style="margin-top:23px">
    <article class="tweet"><div class="avatar" role="img" aria-label="Account avatar photo"></div><span class="name">Brightwave</span><span class="handle">@TheBrightwave</span><span class="date">11 Jul</span><p class="body">Lorem ipsum dolor sit amet, consectetur sadip-iscing elit. Duis suscipit, nisi ut pretium interdum, justo velit fermentum quam.......</p></article>
    <article class="tweet"><div class="avatar" role="img" aria-label="Account avatar photo"></div><span class="name">Brightwave</span><span class="handle">@TheBrightwave</span><span class="date">11 Jul</span><p class="body">Lorem ipsum dolor sit amet, consectetur sadip-iscing elit. Duis suscipit, nisi ut pretium interdum, justo velit fermentum quam.......</p></article>
    <article class="tweet"><div class="avatar" role="img" aria-label="Account avatar photo"></div><span class="name">Brightwave</span><span class="handle">@TheBrightwave</span><span class="date">11 Jul</span><p class="body">Lorem ipsum dolor sit amet, consectetur sadip-iscing elit. Duis suscipit, nisi ut pretium interdum, justo velit fermentum quam.......</p></article>
  </div>
</section>

<section class="abs" style="left:686px;top:318px;width:333px">
  <h3 class="col-heading" style="padding-left:2px">RECENT <em>ACTIVITIES</em>
    <svg class="heading-icon" width="20" height="18" viewBox="0 0 20 18"><g fill="#777"><rect x="0" y="1" width="18" height="2"/><rect x="0" y="5" width="14" height="2"/><rect x="0" y="9" width="18" height="2"/><rect x="0" y="15" width="2" height="2"/><rect x="4" y="15" width="2" height="2"/><rect x="8" y="15" width="2" height="2"/></g></svg></h3>
  <div style="margin-top:0">
    <div class="activity"><svg width="36" height="34" viewBox="0 0 36 34"><path d="M18 3C9 3 3 8 3 15c0 4 2 7 5 9l-2 7 8-5c1 0 3 1 4 1 9 0 15-5 15-12S27 3 18 3z" fill="none" stroke="#5e5e5e" stroke-width="3"/></svg><span class="line">Lorem ipsum dolor sit amet, consecte</span><span class="meta">by<b>Brightwave</b><i>25 minutes ago</i></span></div>
    <div class="activity"><svg width="36" height="34" viewBox="0 0 36 34"><path d="M18 3C9 3 3 8 3 15c0 4 2 7 5 9l-2 7 8-5c1 0 3 1 4 1 9 0 15-5 15-12S27 3 18 3z" fill="none" stroke="#5e5e5e" stroke-width="3"/></svg><span class="line">Lorem ipsum dolor sit amet, consecte</span><span class="meta">by<b>Brightwave</b><i>25 minutes ago</i></span></div>
    <div class="activity"><svg width="36" height="34" viewBox="0 0 36 34"><path d="M18 3C9 3 3 8 3 15c0 4 2 7 5 9l-2 7 8-5c1 0 3 1 4 1 9 0 15-5 15-12S27 3 18 3z" fill="none" stroke="#5e5e5e" stroke-width="3"/></svg><span class="line">Lorem ipsum dolor sit amet, consecte</span><span class="meta">by<b>Brightwave</b><i>25 minutes ago</i></span></div>
  </div>
</section>

<section class="abs" style="left:1064px;top:318px;width:200px">
  <h3 class="col-heading" style="padding-left:2px"><em>NEWS</em>LETTER</h3>
  <p class="newsletter-text" style="margin-top:29px">Vestibulum at lacus id<br>varius. Donec ultricies</p>
  <div class="newsletter-input" style="margin-top:15px"></div>
  <div class="follow" style="margin-top:50px">FOLLOW US <span style="display:inline-block;width:12px;height:16px;background:#ddd;margin-left:22px;vertical-align:-3px"></span></div>
</section>

<div class="abs footer-base"></div>
<span class="abs certificate">CERTIFICATE:</span>
<div class="abs cert-badge" role="img" aria-label="Verified payment badge"></div>

</body>
</html>
```